Need a book cover design for book titled: Resting Beside the River--Simple Methods for the Crossing

This book describes and presents tools to connect with and activate the Lightbody that we all carry within us. It talks about the Lighbody, brief history, lightbody levels and offers exercises to bring light into the body.
I envision a design that shows a physical body changing into light /surrounded by light; a resurrected body ascending to higher dimensions of Spirit o anything comparable .
Updates

Target Market(s)

Mature audience of spiritual seekers and those on spiritual path

Requirements
Must have
• Space on backcover for book summary at top and title and author name on spine.

```html
<!DOCTYPE html>
<html lang="en">
<head>
<meta charset="utf-8">
<title>Resting Beside the River — Cover Spread</title>
<link href="https://fonts.googleapis.com/css2?family=Cinzel:wght@400;600;700&family=Josefin+Sans:wght@300;400&display=swap" rel="stylesheet">
<style>
  :root {
    --page: #ffffff;
    --night: #0a0f2a;
    --night-deep: #050818;
    --night-mid: #101a3c;
    --silver-hi: #ffffff;
    --silver-mid: #b9bec8;
    --silver-lo: #7d8390;
    --sub-blue: #bcd0ff;
    --glow-cyan: #5fe3f5;
    --glow-violet: #8a5cf0;
    --glow-warm: #c9934f;
    --ink-white: #f4f6fb;
  }
  * { margin: 0; padding: 0; box-sizing: border-box; }
  html, body { width: 1200px; height: 1200px; overflow: hidden; background: var(--page); }
  .canvas { position: relative; width: 1200px; height: 1200px; background: var(--page); }

  .spread {
    position: absolute; left: 152px; top: 267px; width: 896px; height: 666px;
    background: radial-gradient(ellipse at 40% 55%, var(--night-mid) 0%, var(--night) 50%, var(--night-deep) 100%);
    overflow: hidden;
  }

  /* back cover */
  .back-cover { position: absolute; left: 0; top: 0; width: 432px; height: 666px; }
  .back-author {
    position: absolute; top: 80px; left: 0; width: 100%; text-align: center;
    font-family: "Josefin Sans", sans-serif; font-weight: 300; font-size: 14px;
    color: var(--ink-white); letter-spacing: 0.5px;
  }
  .back-title { position: absolute; top: 124px; left: 0; width: 100%; text-align: center; }
  .back-title .line-a, .back-title .line-b {
    font-family: "Cinzel", serif; font-weight: 600; line-height: 1;
    background: linear-gradient(180deg, var(--silver-hi) 0%, var(--silver-mid) 55%, var(--silver-lo) 100%);
    -webkit-background-clip: text; background-clip: text; color: transparent;
  }
  .back-title .line-a { font-size: 22px; }
  .back-title .line-b { font-size: 15px; margin-top: 3px; }
  .back-title .subtitle {
    font-family: "Cinzel", serif; font-weight: 700; font-size: 11px;
    color: var(--sub-blue); margin-top: 5px; letter-spacing: 0.3px;
  }
  .back-art {
    position: absolute; left: 0; bottom: 0; width: 432px; height: 170px;
    background:
      radial-gradient(ellipse 30% 32% at 50% 62%, rgba(230,238,255,0.9) 0%, rgba(120,145,230,0.45) 40%, transparent 100%),
      linear-gradient(180deg, transparent 0%, rgba(40,55,120,0.35) 60%, rgba(10,15,42,0.6) 100%);
  }

  /* spine */
  .spine { position: absolute; left: 432px; top: 0; width: 28px; height: 666px; }
  .spine-text {
    position: absolute; left: 14px; top: 133px; transform-origin: 0 0;
    transform: rotate(90deg) translateY(-50%);
    white-space: nowrap; display: flex; align-items: center; gap: 12px;
  }
  .spine-title {
    font-family: "Cinzel", serif; font-weight: 600; font-size: 12.5px;
    background: linear-gradient(180deg, var(--silver-hi), var(--silver-lo));
    -webkit-background-clip: text; background-clip: text; color: transparent;
  }
  .spine-sub { font-family: "Cinzel", serif; font-weight: 700; font-size: 10px; color: var(--sub-blue); }
  .spine-author {
    position: absolute; left: 14px; top: 571px; transform-origin: 0 0;
    transform: rotate(90deg) translateY(-50%); white-space: nowrap;
    font-family: "Josefin Sans", sans-serif; font-weight: 300; font-size: 7.5px; color: var(--ink-white);
  }

  /* front cover */
  .front-cover { position: absolute; left: 460px; top: 0; width: 436px; height: 666px; }
  .front-art {
    position: absolute; left: 34px; top: 0; width: 362px; height: 478px;
    background:
      radial-gradient(ellipse 16% 24% at 64% 42%, rgba(201,147,79,0.75) 0%, rgba(201,147,79,0.25) 60%, transparent 100%),
      radial-gradient(ellipse 12% 20% at 58% 62%, rgba(201,147,79,0.55) 0%, transparent 100%),
      linear-gradient(90deg, transparent 30%, rgba(95,227,245,0.55) 44%, rgba(200,245,255,0.7) 52%, rgba(95,227,245,0.45) 60%, transparent 72%),
      radial-gradient(circle at 78% 70%, rgba(138,92,240,0.55) 0%, transparent 22%),
      radial-gradient(ellipse 50% 40% at 50% 52%, rgba(70,90,170,0.55) 0%, transparent 100%);
    -webkit-mask-image: linear-gradient(180deg, #000 0%, #000 80%, transparent 100%);
            mask-image: linear-gradient(180deg, #000 0%, #000 80%, transparent 100%);
  }
  .front-author {
    position: absolute; top: 24px; left: 0; width: 100%; text-align: center;
    font-family: "Josefin Sans", sans-serif; font-weight: 300; font-size: 23px;
    color: var(--ink-white); padding-left: 10px;
  }
  .front-title { position: absolute; top: 478px; left: 0; width: 100%; text-align: center; }
  .front-title .line-a, .front-title .line-b {
    font-family: "Cinzel", serif; font-weight: 700; line-height: 1;
    background: linear-gradient(180deg, var(--silver-hi) 0%, var(--silver-mid) 50%, var(--silver-lo) 70%, var(--silver-hi) 100%);
    -webkit-background-clip: text; background-clip: text; color: transparent;
  }
  .front-title .line-a { font-size: 56px; }
  .front-title .line-b { font-size: 38px; margin-top: 6px; }
  .front-title .subtitle {
    font-family: "Cinzel", serif; font-weight: 700; font-size: 19px;
    color: var(--sub-blue); margin-top: 12px; letter-spacing: 0.5px;
  }
</style>
</head>
<body>
<div class="canvas">
  <div class="spread">
    <section class="back-cover">
      <p class="back-author">AUTHOR NAME</p>
      <div class="back-title">
        <p class="line-a">RESTING</p>
        <p class="line-b">BESIDE THE RIVER</p>
        <p class="subtitle">Simple Methods for the Crossing</p>
      </div>
      <div class="back-art" role="img" aria-label="Space scene of a planet horizon with a bright sunrise glow"></div>
    </section>

    <section class="spine">
      <div class="spine-text">
        <span class="spine-title">RESTING BESIDE THE RIVER</span>
        <span class="spine-sub">Simple Methods for the Crossing</span>
      </div>
      <p class="spine-author">AUTHOR NAME</p>
    </section>

    <section class="front-cover">
      <div class="front-art" role="img" aria-label="Figure arching upward as it dissolves into a column of cyan and violet light particles over a faint sacred-geometry star"></div>
      <p class="front-author">AUTHOR NAME</p>
      <div class="front-title">
        <p class="line-a">RESTING</p>
        <p class="line-b">BESIDE THE RIVER</p>
        <p class="subtitle">Simple Methods for the Crossing</p>
      </div>
    </section>
  </div>
</div>
</body>
</html>
```